Designs for a Barrister's chambers

Design stationery (including business card and letterhead) for a barrister's chambers -- similar to a law firm, using the enclosed logo. The current designs are not fit for purpose.

```html
<!DOCTYPE html>
<html lang="en">
<head>
<meta charset="utf-8">
<title>Ledgerhall Chambers – Business Card</title>
<link rel="stylesheet" href="https://fonts.googleapis.com/css2?family=Montserrat:wght@600;700&family=Roboto:wght@400&display=swap">
<style>
  :root {
    --navy: #0b1733;
    --teal: #1a8fae;
    --paper: #f4f4f3;
    --ground: #e9e7e5;
    --ink: #2a2f3a;
  }
  * { box-sizing: border-box; margin: 0; padding: 0; }
  html, body { width: 1200px; height: 960px; overflow: hidden; }
  body { background: var(--ground); position: relative; font-family: "Roboto", sans-serif; }

  .card {
    position: absolute;
    width: 540px;
    height: 310px;
    border-radius: 3px;
    box-shadow: 0 14px 30px rgba(0,0,0,0.14), 0 2px 5px rgba(0,0,0,0.08);
    overflow: hidden;
  }

  /* Front */
  .card--front { left: 70px; top: 140px; background: var(--navy); }
  .front-block {
    position: absolute; right: 40px; top: 36px;
    width: 150px; height: 150px; background: var(--teal);
  }
  .front-wordmark {
    position: absolute; left: 44px; bottom: 40px;
    font-family: "Montserrat", sans-serif; font-weight: 700;
    font-size: 34px; line-height: 1.05; color: #ffffff; letter-spacing: -0.5px;
  }

  /* Back */
  .card--back { left: 590px; top: 500px; background: var(--paper); }
  .back-brand {
    position: absolute; left: 36px; top: 108px;
    display: flex; align-items: center; gap: 14px;
  }
  .back-brand__square { width: 50px; height: 50px; background: var(--teal); }
  .back-brand__name {
    font-family: "Montserrat", sans-serif; font-weight: 700;
    font-size: 27px; line-height: 1.02; color: var(--navy); letter-spacing: -0.4px;
  }
  .holder { position: absolute; right: 34px; top: 34px; text-align: right; }
  .holder__name {
    font-family: "Montserrat", sans-serif; font-weight: 700;
    font-size: 14px; color: var(--navy); letter-spacing: 0.3px;
  }
  .holder__role { font-size: 12px; color: var(--teal); margin-top: 1px; }
  .address {
    position: absolute; right: 34px; top: 130px; text-align: right;
    font-size: 11.5px; line-height: 1.4; color: var(--ink);
  }
  .contacts {
    position: absolute; left: 36px; bottom: 30px; list-style: none;
    font-size: 11.5px; line-height: 1.55; color: var(--ink);
  }
  .contacts li { display: flex; align-items: center; gap: 7px; }
  .contacts svg { width: 11px; height: 11px; fill: var(--teal); flex: none; }
</style>
</head>
<body>
  <section class="card card--front" aria-label="Business card front">
    <div class="front-block"></div>
    <p class="front-wordmark">Ledgerhall<br>Chambers</p>
  </section>

  <section class="card card--back" aria-label="Business card back">
    <div class="back-brand">
      <div class="back-brand__square"></div>
      <p class="back-brand__name">Ledgerhall<br>Chambers</p>
    </div>

    <div class="holder">
      <p class="holder__name">MARTIN COLERIDGE</p>
      <p class="holder__role">Barrister</p>
    </div>

    <p class="address">42 Harrow Lane,<br>London&nbsp; EC1X 9ZZ</p>

    <ul class="contacts">
      <li><svg viewBox="0 0 12 12"><path d="M3 0h6a1 1 0 0 1 1 1v10a1 1 0 0 1-1 1H3a1 1 0 0 1-1-1V1a1 1 0 0 1 1-1zm0 1.5v8h6v-8z"/></svg>07000 418 263</li>
      <li><svg viewBox="0 0 12 12"><path d="M1 4c0-2 2-3 5-3s5 1 5 3v1H8V4H4v1H1zM3 6h6l2 5H1z"/></svg>0200 555 0101</li>
      <li><svg viewBox="0 0 12 12"><path d="M3 0h6v4H3zM1 5h10v5H9v2H3v-2H1zm3 3v3h4V8z"/></svg>0200 555 0102</li>
      <li><svg viewBox="0 0 12 12"><path d="M0 2h12v8H0zm1 1v.4l5 3.3 5-3.3V3z"/></svg>martin.coleridge@ledgerhallchambers.com</li>
      <li><svg viewBox="0 0 12 12"><circle cx="6" cy="6" r="6"/></svg>www.ledgerhallchambers.com</li>
    </ul>
  </section>
</body>
</html>
```